Stationery Design Project - New innovative law firm

I need a simple design, yet the tone of the stationery set need to express modern, professionalism, smart and forward-thinking. I don’t need a business card, but require the stationery set to have:
• Design letterhead
• Design facsimile
• Design memo
The triangular logo with Halvard Lane words etc, need to be present in the stationery. The red triangular logo should not be re-designed, but feel free to play around with the placement and colours of the Halvard Lane words etc....?

Target Market(s)

Business clients

Industry/Entity Type

Business

Requirements
Must have
• The triangular logo with Halvard Lane words etc...for branding.

```html
<!DOCTYPE html>
<html lang="en">
<head>
<meta charset="utf-8">
<title>Halvard Lane Stationery Set</title>
<link rel="stylesheet" href="https://fonts.googleapis.com/css2?family=Open+Sans:wght@400;600;700&display=swap">
<style>
:root{
  --backdrop:#676767;
  --paper:#ffffff;
  --brand-red:#d2141e;
  --ink:#1d1d1d;
  --ink-soft:#4a4a4a;
  --rule:#9a9a9a;
  --label:#d9d9d9;
}
*{box-sizing:border-box;margin:0;padding:0}
html,body{width:1200px;height:477px;overflow:hidden}
body{background:var(--backdrop);font-family:"Open Sans",Arial,sans-serif;color:var(--ink);position:relative}
.sheet{position:absolute;background:var(--paper);overflow:hidden}
.sheet--a4{width:276px;height:356px;top:55px}
.sheet--option1{left:47px}
.sheet--option2{left:366px}
.sheet--fax{left:679px}
.sheet--memo{left:982px;top:133px;width:165px;height:212px}
.header{position:absolute;left:0;top:0;width:100%;height:70px}
.sheet--memo .header{height:40px}
.footer{position:absolute;left:0;bottom:0;width:100%;height:12px}
.partners{position:absolute;right:10px;top:5px;text-align:right;color:#fff;font-size:4.6px;line-height:10.5px}
.partners b{font-weight:700;font-size:5.6px}
.partners--compact{font-size:4px;line-height:5.6px;top:5px}
.partners--compact b{font-size:4px;font-weight:600}
.brand{position:absolute;left:16px;top:36px;display:flex;align-items:flex-start;gap:4px}
.brand__mark{width:12px;height:12px;background:var(--brand-red);margin-top:1px}
.brand__name{font-weight:700;font-size:11px;line-height:12px;color:var(--ink);letter-spacing:.2px}
.brand__tagline{font-size:4.4px;color:var(--ink-soft);letter-spacing:.15px;margin-top:1px}
.sheet--memo .brand{left:10px;top:22px;gap:3px}
.sheet--memo .brand__mark{width:8px;height:8px}
.sheet--memo .brand__name{font-size:7px;line-height:8px}
.sheet--memo .brand__tagline{font-size:2.9px}
.t{position:absolute;font-size:3.9px;line-height:5px;white-space:nowrap}
.t--right{text-align:right}
.field{position:absolute;font-size:3.9px;line-height:5px;border-bottom:.5px solid var(--rule);white-space:nowrap;padding-bottom:1px}
.field span{margin-left:20px}
.body-copy{position:absolute;font-size:3.6px;line-height:5.4px;color:var(--ink-soft);white-space:normal}
.fax-title{position:absolute;left:18px;top:76px;font-size:16px;font-weight:400;letter-spacing:.5px}
.check{position:absolute;top:180px;font-size:4px;line-height:5px;display:flex;align-items:center;gap:5px}
.check i{display:block;width:5px;height:5px;border:.6px solid var(--ink)}
.fax-footer{position:absolute;left:0;right:0;bottom:15px;text-align:center;font-size:3.5px}
.web{position:absolute;right:8px;bottom:2.5px;color:#fff;font-size:3.6px;line-height:5px}
.memo-web{position:absolute;right:7px;top:7px;color:#fff;font-size:3px;font-weight:600}
.option-label{position:absolute;top:425px;font-size:11px;color:var(--label)}
</style>
</head>
<body>

<section class="sheet sheet--a4 sheet--option1" aria-label="Letterhead option 1">
  <svg class="header" viewBox="0 0 276 70" preserveAspectRatio="none" aria-hidden="true">
    <path d="M0 0H276V46C215 30 120 24 0 30Z" fill="var(--brand-red)"/>
    <path d="M0 30C120 24 215 30 276 46V55C215 37 120 30 0 33Z" fill="var(--ink)"/>
    <path d="M0 37C120 33 215 42 276 62" fill="none" stroke="var(--rule)" stroke-width=".6"/>
  </svg>
  <div class="partners"><b>Mara Quell,</b> Managing Partner<br><b>Oren Vasko,</b> Managing Partner<br><b>Lidia Ferrow,</b> Partner</div>
  <div class="brand"><div class="brand__mark"></div><div><div class="brand__name">HALVARD LANE</div><div class="brand__tagline">ACCOUNTING, TAX, BUSINESS ADVICE &amp; LEGAL</div></div></div>

  <div class="field" style="left:14px;top:72px;width:128px">Date :<span>01-02-1991</span></div>
  <div class="field" style="left:14px;top:85px;width:128px">Name :</div>
  <div class="field" style="left:14px;top:98px;width:128px">Business :</div>
  <div class="field" style="left:14px;top:111px;width:128px">Address Line1 :</div>
  <div class="field" style="left:14px;top:123px;width:128px">Address Line2 :</div>
  <div class="t t--right" style="right:12px;top:74px">Our Ref: [ADJCT]<br>Your Ref: [Number]</div>
  <div class="t t--right" style="right:12px;top:128px">By (Post/Email/Facsimile Transmission – X Pages)<br>Facsimile No: (07) 1234 5678</div>
  <div class="t" style="left:14px;top:143px">Dear Colleagues,<br>Re: Matter Details.</div>
  <p class="body-copy" style="left:38px;top:166px;width:214px">Lorem ipsum dolor sit amet, consectetuer adipiscing elit, sed diam nonummy nibh euismod tincidunt ut laoreet dolore magna aliquam erat volutpat. Ut wisi enim ad minim veniam, quis nostrud exerci tation ullamcorper suscipit lobortis nisl ut aliquip ex ea commodo consequat. Duis autem vel eum iriure dolor in hendrerit in vulputate velit esse molestie consequat, vel illum dolore eu feugiat nulla facilisis.</p>
  <p class="body-copy" style="left:38px;top:206px;width:214px">Lorem ipsum dolor sit amet, consectetuer adipiscing elit, sed diam nonummy nibh euismod tincidunt ut laoreet dolore magna aliquam erat volutpat. Ut wisi enim ad minim veniam, quis nostrud exerci tation ullamcorper suscipit lobortis nisl ut aliquip ex ea commodo consequat. Duis autem vel eum iriure dolor in hendrerit in vulputate velit esse molestie consequat, vel illum dolore eu feugiat nulla facilisis.</p>
  <div class="t" style="left:14px;top:292px">Yours faithfully</div>
  <div class="t" style="left:14px;top:304px">(Signature)<br>Halvard Lane</div>
  <div class="t" style="left:14px;top:322px">Staff Name<br>Description<br>Writer's Email: Email@halvardlane.example</div>
  <div class="t t--right" style="right:14px;top:301px">Phone : +61 2 9000 1234<br>Mobile : +61 400 111 222<br>E-mail : mara.quell@halvardlane.example</div>
  <div class="t t--right" style="right:14px;top:323px">PO Box 418, Elmstead NSW 2099<br>27 Wrenfield Court, Ashgrove Hill QLD 4119</div>
  <svg class="footer" viewBox="0 0 276 12" preserveAspectRatio="none" aria-hidden="true">
    <rect x="0" y="0" width="276" height="1.2" fill="var(--ink)"/>
    <rect x="0" y="2.4" width="276" height="9.6" fill="var(--ink)"/>
    <path d="M0 2.4H132L120 12H0Z" fill="var(--brand-red)"/>
  </svg>
  <div class="web">www.halvardlane.example</div>
</section>

<section class="sheet sheet--a4 sheet--option2" aria-label="Letterhead option 2">
  <svg class="header" viewBox="0 0 276 70" preserveAspectRatio="none" aria-hidden="true">
    <path d="M0 0H276V46C215 30 120 24 0 30Z" fill="var(--brand-red)"/>
    <path d="M0 30C120 24 215 30 276 46V55C215 37 120 30 0 33Z" fill="var(--ink)"/>
    <path d="M0 37C120 33 215 42 276 62" fill="none" stroke="var(--rule)" stroke-width=".6"/>
  </svg>
  <div class="partners partners--compact"><b>Mara Quell</b> | Managing Partner<br><b>Oren Vasko</b> | Managing Partner<br><b>Lidia Ferrow</b> | Partner<br>PO Box 418, Elmstead NSW 2099<br>27 Wrenfield Court<br>Ashgrove Hill QLD 4119</div>
  <div class="brand"><div class="brand__mark"></div><div><div class="brand__name">HALVARD LANE</div><div class="brand__tagline">ACCOUNTING, TAX, BUSINESS ADVICE &amp; LEGAL</div></div></div>

  <div class="field" style="left:14px;top:72px;width:128px">Date :<span>01-02-1991</span></div>
  <div class="field" style="left:14px;top:85px;width:128px">Name :</div>
  <div class="field" style="left:14px;top:98px;width:128px">Business :</div>
  <div class="field" style="left:14px;top:111px;width:128px">Address Line1 :</div>
  <div class="field" style="left:14px;top:123px;width:128px">Address Line2 :</div>
  <div class="t t--right" style="right:12px;top:74px">Our Ref: [ADJCT]<br>Your Ref: [Number]</div>
  <div class="t t--right" style="right:12px;top:128px">By (Post/Email/Facsimile Transmission – X Pages)<br>Facsimile No: (07) 1234 5678</div>
  <div class="t" style="left:14px;top:143px">Dear Colleagues,<br>Re: Matter Details.</div>
  <p class="body-copy" style="left:40px;top:164px;width:220px">Lorem ipsum dolor sit amet, consectetuer adipiscing elit, sed diam nonummy nibh euismod tincidunt ut laoreet dolore magna aliquam erat volutpat. Ut wisi enim ad minim veniam, quis nostrud exerci tation ullamcorper suscipit lobortis nisl ut aliquip ex ea commodo consequat. Duis autem vel eum iriure dolor in hendrerit in vulputate velit esse molestie consequat, vel illum dolore eu feugiat nulla facilisis.</p>
  <p class="body-copy" style="left:40px;top:203px;width:220px">Lorem ipsum dolor sit amet, consectetuer adipiscing elit, sed diam nonummy nibh euismod tincidunt ut laoreet dolore magna aliquam erat volutpat. Ut wisi enim ad minim veniam, quis nostrud exerci tation ullamcorper suscipit lobortis nisl ut aliquip ex ea commodo consequat. Duis autem vel eum iriure dolor in hendrerit in vulputate velit esse molestie consequat, vel illum dolore eu feugiat nulla facilisis.</p>
  <div class="t" style="left:14px;top:294px">Yours faithfully</div>
  <div class="t" style="left:14px;top:306px">(Signature)<br>Halvard Lane</div>
  <div class="t" style="left:14px;top:323px">Staff Name<br>Description<br>Writer's Email: Email@halvardlane.example</div>
  <div class="t t--right" style="right:14px;top:301px">Phone : +61 2 9000 1234<br>Mobile : +61 400 111 222<br>Web : www.halvardlane.example</div>
  <div class="t t--right" style="right:14px;top:323px">PO Box 418, Elmstead NSW 2099<br>27 Wrenfield Court, Ashgrove Hill QLD 4119</div>
  <svg class="footer" viewBox="0 0 276 12" preserveAspectRatio="none" aria-hidden="true">
    <path d="M0 5H140L132 12H0Z" fill="var(--brand-red)"/>
    <path d="M136 12L144 5H276V12Z" fill="var(--ink)"/>
  </svg>
</section>

<section class="sheet sheet--a4 sheet--fax" aria-label="Facsimile">
  <svg class="header" viewBox="0 0 276 70" preserveAspectRatio="none" aria-hidden="true">
    <path d="M0 0H276V46C215 30 120 24 0 30Z" fill="var(--brand-red)"/>
    <path d="M0 30C120 24 215 30 276 46V55C215 37 120 30 0 33Z" fill="var(--ink)"/>
    <path d="M0 37C120 33 215 42 276 62" fill="none" stroke="var(--rule)" stroke-width=".6"/>
  </svg>
  <div class="partners partners--compact"><b>Mara Quell</b> | Managing Partner<br><b>Oren Vasko</b> | Managing Partner<br><b>Lidia Ferrow</b> | Partner<br>PO Box 418, Elmstead NSW 2099<br>27 Wrenfield Court<br>Ashgrove Hill QLD 4119</div>
  <div class="brand"><div class="brand__mark"></div><div><div class="brand__name">HALVARD LANE</div><div class="brand__tagline">ACCOUNTING, TAX, BUSINESS ADVICE &amp; LEGAL</div></div></div>
  <div class="fax-title">FAX</div>

  <div class="field" style="left:18px;top:108px;width:122px">To :<span>(Recipient name)</span></div>
  <div class="field" style="left:18px;top:122px;width:122px">Fax :<span>(Recipient fax number)</span></div>
  <div class="field" style="left:18px;top:136px;width:122px">Phone :<span>(Recipient phone number)</span></div>
  <div class="field" style="left:18px;top:151px;width:122px">Re :<span>(Subject)</span></div>
  <div class="field" style="left:161px;top:108px;width:98px">From :<span>(Your name)</span></div>
  <div class="field" style="left:161px;top:122px;width:98px">Pages :<span>(Number of pages)</span></div>
  <div class="field" style="left:161px;top:136px;width:98px">Date :<span>(Pick the date)</span></div>
  <div class="field" style="left:161px;top:151px;width:98px">CC :<span>(Name)</span></div>

  <div class="check" style="left:18px"><i></i>Urgent</div>
  <div class="check" style="left:56px"><i></i>For Review</div>
  <div class="check" style="left:104px"><i></i>Please Comment</div>
  <div class="check" style="left:162px"><i></i>Please Reply</div>
  <div class="check" style="left:215px"><i></i>Please Recycle</div>

  <div class="t" style="left:18px;top:198px">Dear Sir :</div>
  <p class="body-copy" style="left:36px;top:209px;width:220px">Lorem ipsum dolor sit amet, consectetuer adipiscing elit, sed diam nonummy nibh euismod tincidunt ut laoreet dolore magna aliquam erat volutpat. Ut wisi enim ad minim veniam, quis nostrud exerci tation ullamcorper suscipit lobortis nisl ut aliquip ex ea commodo consequat. Duis autem vel eum iriure dolor in hendrerit in vulputate velit esse molestie consequat, vel illum dolore eu feugiat nulla facilisis.</p>
  <div class="t" style="left:18px;top:283px">Yours faithfully</div>
  <div class="t" style="left:18px;top:294px">(Signature)<br>Halvard Lane</div>
  <div class="field" style="left:18px;top:314px;width:118px">Per :</div>
  <div class="field" style="left:150px;top:314px;width:108px">Position :</div>
  <div class="fax-footer">Phone : +61 2 9000 1234 &nbsp; Mobile : +61 400 111 222 &nbsp; E-mail : mara.quell@halvardlane.example &nbsp; Web : www.halvardlane.example</div>
  <svg class="footer" viewBox="0 0 276 12" preserveAspectRatio="none" aria-hidden="true">
    <path d="M0 5H140L132 12H0Z" fill="var(--brand-red)"/>
    <path d="M136 12L144 5H276V12Z" fill="var(--ink)"/>
  </svg>
</section>

<section class="sheet sheet--memo" aria-label="Memo">
  <svg class="header" viewBox="0 0 165 40" preserveAspectRatio="none" aria-hidden="true">
    <path d="M0 0H165V28C128 18 72 14 0 18Z" fill="var(--brand-red)"/>
    <path d="M0 18C72 14 128 18 165 28V33C128 22 72 18 0 20Z" fill="var(--ink)"/>
    <path d="M0 23C72 20 128 25 165 37" fill="none" stroke="var(--rule)" stroke-width=".5"/>
  </svg>
  <div class="memo-web">www.halvardlane.example</div>
  <div class="brand"><div class="brand__mark"></div><div><div class="brand__name">HALVARD LANE</div><div class="brand__tagline">ACCOUNTING, TAX, BUSINESS ADVICE &amp; LEGAL</div></div></div>
  <div class="t" style="left:10px;top:49px;font-size:3.2px">Date : &nbsp;&nbsp;&nbsp;&nbsp;&nbsp; 01-02-1991</div>
  <div class="t" style="left:10px;top:63px;font-size:3.2px">Dear Colleagues,<br>Re: Matter Details.</div>
  <p class="body-copy" style="left:10px;top:94px;width:146px;font-size:3px;line-height:4.5px">Lorem ipsum dolor sit amet, consectetuer adipiscing elit, sed diam nonummy nibh euismod tincidunt ut laoreet dolore magna aliquam erat volutpat. Ut wisi enim ad minim veniam, quis nostrud exerci tation ullamcorper suscipit lobortis nisl ut aliquip ex ea commodo consequat. Duis autem vel eum iriure dolor in hendrerit in vulputate velit esse molestie consequat, vel illum dolore eu feugiat nulla facilisis.</p>
  <div class="t" style="left:10px;top:180px;font-size:3.2px">Yours faithfully</div>
  <div class="t" style="left:10px;top:191px;font-size:3.2px;line-height:4.4px">(Signature)<br>Halvard Lane</div>
</section>

<div class="option-label" style="left:160px">Option 1</div>
<div class="option-label" style="left:496px">Option 2</div>

</body>
</html>
```